Scented Candle Company Sticker Design for Packaging

We need a Sticker design for our various scented candle packages. Our handmade candles incorperate hand crafted Chiyogami Paper imported from Japan, which is wrapped around the jar. Each of the scents have different papers assigned to them and although we would like a general design in which the text can be changed according to each scent we would also like if the beautiful Japanese paper designs could be subtly incorporated in the design.

We want the the text of the sticker and logo of our company to be printed in gold foil once printed and our featured logo image is of a Dogwood tree. We think that perhaps the inclusion of dogwood blossom/s might look nice in the design but is not a must have!

We are fond of the delicate and classic print designs and etching designs. We would also like the design to be in a portrait rectangle that is closer in the shape of a square/ or not too long of a rectangle, and, would like to have a boarder on the edge of the sticker (this could incorporate the blossom if you wish, I have attached an image for reference/ inspiration) but we are after something much more simplistic and draws less attention to the eye and connected in the boarder.

Our brand is elegant and classic and we would like to be in keeping with our style. We have attached some images of the candles and our logo for inspiration, we do not want the stickers for the candle themselves but rather to place on the packaging.

Ive left some information for one of the candle scents for this design but once again I would like to reiterate that the design should allow for interchangeable titles for the other fragrances.

Japanese Cherry Blossom(in smaller writing).
Japanese cherry blossom, Orange blossom, cinnamon.

Our candles are hand made in Australia and a made from 100% soy wax and we would like to to be presented on the label.

I would like to mention again that we are looking for an elegant and classic design. We are looking for a simplistic design/layout that also focuses on the fine details. It should be striking but also not overbearing with an air of sophistication with minimal to no use of colours in encouraged.

I have also attached a font that is matched to the "candle co." underneath the tree in the logo.
Updates

I only just posted the design request, but first created the brief on the 2nd. I would like more time for the designers to both see my review and have an adequate amount of time to work on the project.

Target Market(s)

Up Market Shoppers.

Font styles to use
Script
Other font styles liked:
• Acorn

Colors
fbfbfb

Requirements
Must have
• Logo on the sticker.
Nice to have
• Nice to have a dogwood blossom incorporated into the boarder but must be simplistic as it doesn't want to be the main focus of the sticker
Should not have
• Photographs in the sticker design. Must be graphic design. No to little colour.

```html
<!DOCTYPE html>
<html lang="en">
<head>
<meta charset="utf-8">
<title>Larchmere Candle Co. – Japanese Cherry Blossom Label</title>
<link rel="stylesheet" href="https://fonts.googleapis.com/css2?family=Questrial&family=Lato:wght@400&display=swap">
<style>
  :root {
    --page: #ffffff;
    --label: #ffffff;
    --ink: #111111;
    --gold: #e9bb52;
    --leaf-deep: #5f8a63;
    --leaf-mid: #8fae84;
    --leaf-pale: #c3d4bb;
    --leaf-blue: #6f8ea3;
  }
  * { margin: 0; padding: 0; box-sizing: border-box; }
  html, body {
    width: 1034px;
    height: 1200px;
    overflow: hidden;
    background: var(--page);
  }
  .sticker {
    position: relative;
    width: 1034px;
    height: 1200px;
    background: var(--page);
  }
  .foliage {
    position: absolute;
    left: 40px;
    top: 150px;
    width: 930px;
    height: 915px;
  }
  .label-card {
    position: absolute;
    left: 240px;
    top: 336px;
    width: 549px;
    height: 548px;
    background: var(--label);
  }
  .gold-frame {
    position: absolute;
    left: 16px;
    top: 22px;
    width: 504px;
    height: 501px;
    border: 6px solid var(--gold);
  }
  .brand {
    position: absolute;
    left: 0;
    width: 100%;
    text-align: center;
    font-family: "Questrial", sans-serif;
    color: var(--ink);
  }
  .brand-name {
    top: 132px;
    font-size: 27px;
    letter-spacing: 4px;
  }
  .brand-sub {
    top: 168px;
    font-size: 10px;
    letter-spacing: 1.5px;
  }
  .scent-title {
    position: absolute;
    left: 0;
    top: 258px;
    width: 100%;
    text-align: center;
    font-family: "Questrial", sans-serif;
    font-size: 34px;
    line-height: 39px;
    color: var(--ink);
  }
  .origin-note {
    position: absolute;
    left: 0;
    top: 408px;
    width: 100%;
    text-align: center;
    font-family: "Lato", sans-serif;
    font-size: 13.5px;
    line-height: 19px;
    color: var(--ink);
  }
</style>
</head>
<body>
  <main class="sticker">
    <svg class="foliage" viewBox="0 0 930 915" role="img" aria-label="Watercolour wreath of eucalyptus, olive and fern leaves with blue berries framing the label">
      <defs>
        <radialGradient id="leafWash" cx="50%" cy="50%" r="55%">
          <stop offset="0%" stop-color="var(--leaf-mid)"/>
          <stop offset="55%" stop-color="var(--leaf-deep)"/>
          <stop offset="80%" stop-color="var(--leaf-mid)" stop-opacity="0.7"/>
          <stop offset="100%" stop-color="var(--leaf-pale)" stop-opacity="0"/>
        </radialGradient>
      </defs>
      <ellipse cx="465" cy="457" rx="465" ry="457" fill="url(#leafWash)"/>
    </svg>

    <section class="label-card">
      <div class="gold-frame"></div>
      <p class="brand brand-name">LARCHMERE</p>
      <p class="brand brand-sub">CANDLE CO.</p>
      <h1 class="scent-title">JAPANESE<br>CHERRY BLOSSOM</h1>
      <p class="origin-note">Our candles are hand made in Australia<br>&amp;<br>Made from 100% soy wax.</p>
    </section>
  </main>
</body>
</html>
```